Breezy Trinkets Handcrafted Copper Jewelry

I make handcrafted copper bracelets and cuffs.
I need a banner made (2' 1/2" x 10')
I attached the logo (I would like that sketch to be purple)
Company name: Breezy Trinkets (in a "sassy" font)
Tag line: Wear your Breeze
Designer/Creator: Norma Tillery
481.307.6624
FB: www.facebook.com/breezytrinkets.example
shop.breezytrinkets.example
I'd like the background to be white. I'm not sure what I'm looking for as far as the look or if I should add any pics of the copper jewelry that I make. I'm totally up for suggestions. I'm very eager to see how creative you can be.
Many thanks.
Jewelry

```html
<!DOCTYPE html>
<html lang="en">
<head>
<meta charset="utf-8">
<title>Breezy Trinkets – Banner</title>
<link rel="stylesheet" href="https://fonts.googleapis.com/css2?family=Courgette&display=swap">
<style>
  :root {
    --paper: #ffffff;
    --brand-purple: #7b4aa6;
    --sketch-light: #f1eaf7;
    --sketch-mid: #ddcbeb;
  }
  html, body {
    margin: 0;
    padding: 0;
    overflow: hidden;
    background: var(--paper);
  }
  .banner {
    position: relative;
    width: 1200px;
    height: 300px;
    background: var(--paper);
    overflow: hidden;
  }
  .figure-sketch {
    position: absolute;
    top: 14px;
    width: 130px;
    height: 272px;
    border-radius: 60px 60px 20px 20px;
    background: linear-gradient(180deg, var(--sketch-light) 0%, var(--sketch-mid) 55%, var(--sketch-light) 100%);
  }
  .figure-sketch--left { left: 60px; }
  .figure-sketch--right { left: 1010px; }
  .brand {
    position: absolute;
    left: 0;
    top: 0;
    width: 1200px;
    text-align: center;
    font-family: "Courgette", cursive;
    color: var(--brand-purple);
  }
  .brand-name {
    position: absolute;
    left: 0;
    top: 44px;
    width: 100%;
    margin: 0;
    font-size: 78px;
    font-weight: 400;
    line-height: 1;
    letter-spacing: 1px;
  }
  .brand-tagline {
    position: absolute;
    left: 0;
    top: 170px;
    width: 100%;
    margin: 0;
    font-size: 52px;
    font-weight: 400;
    line-height: 1;
  }
</style>
</head>
<body>
  <main class="banner">
    <div class="figure-sketch figure-sketch--left" role="img" aria-label="Purple line sketch of a woman in a flowing strapless dress and boots"></div>
    <div class="brand">
      <h1 class="brand-name">Breezy Trinkets</h1>
      <p class="brand-tagline">Wear your Breeze</p>
    </div>
    <div class="figure-sketch figure-sketch--right" role="img" aria-label="Purple line sketch of a woman in a flowing strapless dress and boots"></div>
  </main>
</body>
</html>
```